Wendlow Superfoods Packaging Design

We are looking for a design for our premium superfoods powders and blends. Packaging dimensions are 21cm x 13cm Kraft packaging (light brown background). This design should be a blueprint for other products that we will be marketing including lions mane mushroom, reishi mushroom, Chaga mushroom, Spirilina, bee pollen, açai powder and the like. The design should be clean but earthy, and the template replicable for other products.

```html
<!DOCTYPE html>
<html lang="en">
<head>
<meta charset="utf-8">
<title>Wendlow Superfoods – Moringa Leaf Pouch</title>
<link rel="stylesheet" href="https://fonts.googleapis.com/css2?family=Montserrat:wght@800&family=Roboto:wght@400;500&family=Courgette&family=Tinos&display=swap">
<style>
  :root {
    --backdrop: #ededed;
    --pouch-green: #3f6a37;
    --pouch-green-dark: #345c2e;
    --pouch-green-light: #4a7741;
    --label-white: #f4f4f2;
    --brand-ink: #2e2e2e;
    --brand-leaf: #4f8a3a;
    --title-grey: #e6e6e6;
    --text-white: #ffffff;
    --accent-green: #86c04f;
  }
  html, body {
    margin: 0;
    width: 1126px;
    height: 1200px;
    overflow: hidden;
    background: var(--backdrop);
  }
  .pouch {
    position: absolute;
    left: 263px;
    top: 55px;
    width: 600px;
    height: 1090px;
    background: linear-gradient(160deg, var(--pouch-green-light) 0%, var(--pouch-green) 45%, var(--pouch-green-dark) 100%);
    overflow: hidden;
    font-family: "Roboto", Arial, sans-serif;
  }
  .tear-notch {
    position: absolute;
    top: 150px;
    width: 14px;
    height: 14px;
    background: var(--backdrop);
    border-radius: 50%;
  }
  .tear-notch--left { left: -7px; }
  .tear-notch--right { right: -7px; }
  .botanical-art {
    position: absolute;
    left: 110px;
    top: 220px;
    width: 460px;
    height: 700px;
    background: radial-gradient(ellipse at 60% 40%, rgba(255,255,255,0.07), rgba(255,255,255,0) 70%);
  }
  .brand-label {
    position: absolute;
    left: 127px;
    top: 34px;
    width: 340px;
    height: 103px;
    background: var(--label-white);
    display: flex;
    align-items: center;
    justify-content: center;
    gap: 8px;
  }
  .brand-name {
    font-family: "Courgette", cursive;
    font-size: 44px;
    color: var(--brand-ink);
    line-height: 1;
  }
  .brand-dot {
    width: 12px;
    height: 12px;
    border-radius: 50%;
    background: var(--brand-leaf);
    margin-top: -28px;
  }
  .product-name {
    position: absolute;
    left: 34px;
    top: 828px;
    transform-origin: 0 0;
    transform: rotate(-90deg);
    margin: 0;
    font-family: "Montserrat", Arial, sans-serif;
    font-weight: 800;
    font-size: 96px;
    letter-spacing: 3px;
    line-height: 1;
    color: var(--title-grey);
    white-space: nowrap;
  }
  .product-type {
    position: absolute;
    left: 144px;
    top: 462px;
    margin: 0;
    font-weight: 500;
    font-size: 92px;
    line-height: 1;
    color: var(--text-white);
  }
  .product-range {
    position: absolute;
    left: 146px;
    top: 558px;
    margin: 0;
    font-weight: 500;
    font-size: 33px;
    color: var(--accent-green);
  }
  .benefit-list {
    position: absolute;
    left: 146px;
    top: 604px;
    margin: 0;
    padding: 0;
    list-style: none;
    color: var(--text-white);
    font-size: 20px;
    line-height: 26px;
  }
  .benefit-list li::before {
    content: "•";
    margin-right: 8px;
  }
  .product-story {
    position: absolute;
    left: 130px;
    top: 740px;
    width: 415px;
    margin: 0;
    font-family: "Tinos", serif;
    font-size: 12.5px;
    line-height: 17px;
    color: var(--text-white);
  }
  .net-weight {
    position: absolute;
    left: 340px;
    top: 868px;
    margin: 0;
    font-size: 25px;
    color: var(--text-white);
  }
</style>
</head>
<body>
  <main class="pouch">
    <span class="tear-notch tear-notch--left"></span>
    <span class="tear-notch tear-notch--right"></span>
    <div class="botanical-art" role="img" aria-label="Faint line drawing of moringa leaves and branches"></div>

    <div class="brand-label">
      <span class="brand-name">wendlow</span>
      <span class="brand-dot"></span>
    </div>

    <h1 class="product-name">MORINGA</h1>
    <h2 class="product-type">Leaf</h2>
    <p class="product-range">Superfoods</p>

    <ul class="benefit-list">
      <li>7x The Vitamin C Of Oranges</li>
      <li>4x The Calcium Of Milk</li>
      <li>3x The Potassium Of Bananas</li>
      <li>3x Iron Of Spinach</li>
    </ul>

    <p class="product-story">The Leaves Contain All Nine Essential Amino Acids And Traditionally Used In Assisting The Healing Of Many Ailments. The Nutritional Diversity Is Also Known To Reduce Both Cholesterol And Blood Sugar Levels Whilst Also Have Serious Anti-inflammatory Benefits. Our 100% Organic Moringa Is Grown And Harvested In Its Native Environment, Supporting Premium Superfood Nutrition</p>

    <p class="net-weight">Net Wt 250g</p>
  </main>
</body>
</html>
```